Flyer Design

A flyer to introduce our new business called Smilebirds on Wheels ,we are a mobile dental hygienist service based in the Teesside area of England.We use portable equipment to treat clients where they live or work Since may 2013 in the uk hygienists no longer need to work with a dentist ,therefore clients can now access dental hygiene care without seeing a dentist.We offer scale and polish ,oral hygiene advice .Our colours are pink,green and purple.we would like to stress the importance of a regular professional clean with the convenience of being treated at home

Target Market(s)

over 18 years of age who choose or need to have there scale and polish at home

Industry/Entity Type

Dental

Colors
e34297
9ccb3b
876aae

Requirements
Must have
• ,must have our logo and our contact details tel 07481236905 and email info@smilebirdsonwheels.co.uk
The hygienists names Helen Marbury and Dawn Pickett
eye catching and colourful ,not to many words,but getting across we are for anyone who chooses or needs their treatment at home
Nice to have
• we would like the logo to be prominent ,our colours are pink ,green and purple .the font easy to read for older people
Should not have
• A lot of writing on the front the page ,

```html
<!DOCTYPE html>
<html lang="en">
<head>
<meta charset="utf-8">
<title>Smilebirds on Wheels – Flyer</title>
<link rel="stylesheet" href="https://fonts.googleapis.com/css2?family=Carlito:wght@400;700&family=Arimo:wght@400&display=swap">
<style>
  :root {
    --field-green: #7ab96a;
    --ground-pink: #cf74a8;
    --device-dark: #161616;
    --device-rim: #bdbdbd;
    --screen-white: #f4f1f1;
    --brand-pink: #d9578f;
    --brand-green: #5cae47;
    --ink: #111111;
    --brush-dark: #0c2a10;
  }
  html, body { margin: 0; padding: 0; overflow: hidden; }
  .flyer {
    position: relative;
    width: 932px;
    height: 1200px;
    overflow: hidden;
    background: linear-gradient(to bottom, var(--field-green) 0 958px, var(--ground-pink) 958px 100%);
    font-family: "Carlito", "Calibri", sans-serif;
  }
  .brush {
    position: absolute;
    top: 801px;
    width: 194px;
    height: 185px;
    background: linear-gradient(to bottom, var(--brush-dark), #1f4a22 70%, #3a1a2c);
    border-radius: 40px 40px 6px 6px;
  }
  .brush--left { left: 0; border-top-left-radius: 6px; }
  .brush--right { right: 0; border-top-right-radius: 6px; }
  .device {
    position: absolute;
    left: 198px;
    top: 90px;
    width: 538px;
    height: 1019px;
    border-radius: 74px;
    background: linear-gradient(135deg, #2a2a2a, var(--device-dark) 60%);
    box-shadow: 0 0 0 7px var(--device-rim);
  }
  .screen {
    position: absolute;
    left: 228px;
    top: 250px;
    width: 471px;
    height: 700px;
    background: var(--screen-white);
    text-align: center;
    color: var(--ink);
  }
  .brand {
    position: absolute;
    top: 48px;
    left: 0;
    width: 100%;
  }
  .brand__name {
    display: flex;
    align-items: center;
    justify-content: center;
    gap: 8px;
    font-size: 22px;
    color: var(--brand-pink);
    line-height: 1;
  }
  .brand__dot {
    width: 14px;
    height: 14px;
    border-radius: 50%;
    background: var(--brand-green);
  }
  .brand__tagline {
    margin-top: 54px;
    font-size: 15px;
    color: var(--brand-green);
    font-family: "Arimo", "Arial", sans-serif;
  }
  .intro {
    position: absolute;
    top: 198px;
    left: 0;
    width: 100%;
    margin: 0;
    font-size: 18px;
    line-height: 25.2px;
  }
  .contact {
    position: absolute;
    top: 603px;
    left: 0;
    width: 100%;
    margin: 0;
    font-size: 18px;
    line-height: 25px;
    font-style: normal;
  }
</style>
</head>
<body>
<main class="flyer">
  <div class="brush brush--left" role="img" aria-label="Illustrated toothbrush head with toothpaste"></div>
  <div class="brush brush--right" role="img" aria-label="Illustrated toothbrush head with toothpaste"></div>
  <div class="device" role="img" aria-label="Illustrated smartphone body"></div>

  <section class="screen">
    <header class="brand">
      <div class="brand__name"><span>Smilebirds on Wheels</span><span class="brand__dot"></span></div>
      <div class="brand__tagline">Mobile Dental Hygienists</div>
    </header>

    <p class="intro">
      Smilebirds on Wheels is a mobile dental<br>
      hygienist service based in Teesside. We use<br>
      portable equipment to treat you either in<br>
      your place of residence or work place. Since<br>
      May 2013, the UK hygienists no longer need<br>
      to work with a dentist, meaning you can<br>
      now access dental hygiene care without<br>
      seeing a dentist. Our mobile service offers<br>
      scale and polish as well as oral hygiene<br>
      advice .We would like to stress the impor-<br>
      tance of a regular professional clean with<br>
      the convenience of being treated in a com-<br>
      fortable and familiar environment.
    </p>

    <address class="contact">
      07481236905<br>
      @smilebirdsonwheels.co.uk<br>
      Hygienists: Helen Marbury and Dawn Pickett
    </address>
  </section>
</main>
</body>
</html>
```